Business Card for Bright Furrow Lawn & Landscape

Double Sided Card Design - I think one side of the card should be cleaner, with logo, contact info, and "Complete Residential & Commercial Landscape Services", and on the other side it should list the services we offer:

- Lawn Care & Mowing
- Hedge & Shrub Trimming
- Leaf Removal & Clean Up
- Aeration & Sod
- Mulch & Rock Installations
- Landscape Installations & Renovations
- Commercial Snow Removal

Please make it clean and very professional... don't want it too be too busy, but want to tell them what we do.

Target Market(s)

Residential and Commercial

Industry/Entity Type

Landscape

Contact Information for Business Card

Fully Insured
Dale Ostrov
410-372-6184
Dostrov07@quillpost.net

Requirements
Must have
• Double Sided, Cleaner on one side, more information and text on the other side.

```html
<!DOCTYPE html>
<html lang="en">
<head>
<meta charset="utf-8">
<title>Bright Furrow Lawn &amp; Landscape – Business Card</title>
<link rel="stylesheet" href="https://fonts.googleapis.com/css2?family=Roboto:wght@300;400;500&display=swap">
<style>
  :root {
    --lime: #8cbf3f;
    --lime-light: #d9ecb8;
    --charcoal: #25282a;
    --charcoal-soft: #2f3335;
    --stroke-grey: #5a5f62;
    --paper: #e9ebe8;
    --backdrop: #3a3d3f;
    --ink: #1c1e1f;
  }
  * { margin: 0; padding: 0; box-sizing: border-box; }
  html, body { width: 1200px; height: 959px; overflow: hidden; }
  body {
    background: var(--backdrop);
    font-family: "Roboto", Arial, sans-serif;
    position: relative;
  }
  .card {
    position: absolute;
    left: 240px;
    width: 720px;
    height: 411px;
    overflow: hidden;
  }
  /* ---------- Services side ---------- */
  .card-services { top: 50px; background: var(--lime); }
  .services-panel {
    position: absolute;
    inset: 24px;
    background: var(--charcoal);
  }
  .services-frame {
    position: absolute;
    left: 48px; right: 48px; top: 56px; bottom: 52px;
    border: 2px solid var(--lime);
  }
  .frame-tab {
    position: absolute;
    width: 6px; height: 70px;
    background: var(--lime);
    top: 50%; transform: translateY(-50%);
  }
  .frame-tab.left { left: -4px; }
  .frame-tab.right { right: -4px; }
  .services-title {
    position: absolute;
    top: -16px; left: 50%;
    transform: translateX(-50%);
    background: var(--charcoal);
    padding: 0 12px;
    color: var(--lime);
    font-size: 25px;
    font-weight: 400;
    letter-spacing: 0.5px;
    white-space: nowrap;
  }
  .services-list {
    position: absolute;
    top: 46px; left: 0; right: 0;
    text-align: center;
    color: var(--paper);
    font-size: 17px;
    line-height: 31px;
    font-weight: 400;
  }
  .bullet { color: var(--lime); margin: 0 4px; }
  /* ---------- Contact side ---------- */
  .card-contact { top: 498px; background: var(--lime); }
  .wave { position: absolute; inset: 0; }
  .fully-insured {
    position: absolute;
    top: 52px; left: 418px;
    color: var(--lime-light);
    font-size: 19px;
    letter-spacing: 1px;
    font-weight: 400;
  }
  .name {
    position: absolute;
    top: 118px; left: 46px;
    display: flex; align-items: center; gap: 12px;
    color: var(--paper);
    font-size: 44px;
    font-weight: 300;
  }
  .name-bar { width: 9px; height: 34px; background: var(--charcoal); }
  .contact-lines {
    position: absolute;
    top: 200px; left: 66px;
    color: var(--paper);
    font-size: 19px;
    line-height: 32px;
    font-weight: 400;
  }
  .tagline {
    position: absolute;
    top: 296px; left: 66px;
    color: var(--ink);
    font-size: 15px;
    line-height: 22px;
    font-weight: 400;
  }
  .brand {
    position: absolute;
    top: 168px; left: 480px;
    width: 210px;
    text-align: center;
    color: var(--paper);
    font-weight: 500;
  }
  .brand-dot {
    width: 74px; height: 74px;
    border-radius: 50%;
    background: var(--lime);
    margin: 0 auto 14px;
  }
  .brand-name { font-size: 28px; letter-spacing: 1px; line-height: 32px; }
  .brand-sub { font-size: 14px; letter-spacing: 3px; line-height: 22px; }
</style>
</head>
<body>
  <section class="card card-services">
    <div class="services-panel">
      <div class="services-frame">
        <span class="frame-tab left"></span>
        <span class="frame-tab right"></span>
        <h2 class="services-title">SERVICES WE OFFER:</h2>
        <p class="services-list">
          <span class="bullet">•</span>Lawn Care &amp; Mowing <span class="bullet">•</span>Hedge &amp; Shrub Trimming<br>
          <span class="bullet">•</span>Leaf Removal &amp; Clean Up <span class="bullet">•</span>Aeration &amp; Sod<br>
          <span class="bullet">•</span>Mulch &amp; Rock Installations<br>
          <span class="bullet">•</span>Landscape Installations &amp; Renovations<br>
          <span class="bullet">•</span>Commercial Snow Removal
        </p>
      </div>
    </div>
  </section>

  <section class="card card-contact">
    <svg class="wave" width="720" height="411" viewBox="0 0 720 411" aria-hidden="true">
      <path d="M40 411 C170 385 370 395 395 270 C420 140 480 40 610 0 L720 0 L720 411 Z" fill="var(--stroke-grey)"/>
      <path d="M62 411 C190 392 392 400 417 272 C442 148 500 50 630 0 L720 0 L720 411 Z" fill="var(--charcoal)"/>
      <path d="M630 0 L720 0 L720 411 L420 411 Z" fill="var(--charcoal-soft)" opacity="0.35"/>
    </svg>
    <p class="fully-insured">FULLY INSURED</p>
    <h1 class="name"><span class="name-bar"></span>Dale Ostrov</h1>
    <p class="contact-lines">P: 410-372-6184<br>E: Dostrov07@quillpost.net</p>
    <p class="tagline">Complete Residential &amp; Commercial<br>Landscape Services</p>
    <div class="brand">
      <div class="brand-dot"></div>
      <div class="brand-name">BRIGHT FURROW</div>
      <div class="brand-sub">LAWN &amp; LANDSCAPE</div>
    </div>
  </section>
</body>
</html>
```